Financial Advisor needs a NEW business card design

We need a new card design as our current design has no white space and clients tend to want to write on the card. I am attaching our current logos and current card design. I have also played with some designs I liked online but don't have the knowledge (or software) to complete the designs in a format that is appropriate for production. I've attached those designs that I liked too. With two office locations and a disclaimer there is a lot of info but we want it to look tidy. We like the deep, rich blue colors and want it to look clean, strong, and modern yet classic.
Business
Included in the attached files

```html
<!DOCTYPE html>
<html lang="en">
<head>
<meta charset="utf-8">
<title>Norland Advisory – Business Card</title>
<link href="https://fonts.googleapis.com/css2?family=Cinzel:wght@400;600&display=swap" rel="stylesheet">
<style>
  :root {
    --navy: #0b2a4a;
    --paper: #f7f7f5;
    --ink: #1f2b3a;
    --grey-text: #8c9199;
    --light-on-navy: #e9edf2;
    --muted-on-navy: #9aa6b4;
    --backdrop: #d9d9d7;
  }
  * { margin: 0; padding: 0; box-sizing: border-box; }
  html, body {
    width: 1200px; height: 1029px; overflow: hidden;
    background: var(--backdrop);
    font-family: "Cinzel", "Times New Roman", serif;
  }
  .sheet {
    width: 1200px; height: 1029px;
    display: flex; flex-direction: column; align-items: center; justify-content: center;
    gap: 40px;
  }
  .card {
    position: relative; width: 800px; height: 457px;
    background: var(--paper);
    box-shadow: 0 6px 18px rgba(0,0,0,.18);
    overflow: hidden;
  }

  /* Front */
  .card-front .edge { position: absolute; top: 0; bottom: 0; width: 14px; background: var(--navy); }
  .card-front .edge-left { left: 0; }
  .card-front .edge-right { right: 0; }
  .front-brand {
    position: absolute; top: 70px; left: 0; right: 0; text-align: center;
    color: var(--navy); font-weight: 600; font-size: 40px; letter-spacing: 2px; line-height: 1.1;
  }
  .front-brand small { display: block; font-size: 22px; letter-spacing: 3px; }
  .disclaimer {
    position: absolute; top: 215px; left: 90px; right: 90px; text-align: center;
    color: var(--ink); font-size: 13px; letter-spacing: 2.5px; line-height: 1.6; text-transform: uppercase;
  }
  .front-web {
    position: absolute; bottom: 80px; left: 0; right: 0; text-align: center;
    color: var(--ink); font-size: 14px; letter-spacing: 4px; text-transform: uppercase;
  }

  /* Back */
  .back-panel {
    position: absolute; left: 0; top: 0; bottom: 0; width: 455px; background: var(--navy);
  }
  .person { position: absolute; top: 85px; left: 70px; }
  .person-name { color: var(--light-on-navy); font-size: 24px; letter-spacing: 3px; text-transform: uppercase; }
  .person-title { color: var(--muted-on-navy); font-size: 15px; letter-spacing: 4px; text-transform: uppercase; margin-top: 2px; }
  .contacts { position: absolute; top: 230px; left: 55px; list-style: none; }
  .contacts li {
    display: flex; gap: 18px; align-items: flex-start;
    color: var(--light-on-navy); font-size: 13px; letter-spacing: 1px; line-height: 1.5; margin-bottom: 16px;
  }
  .contacts svg { width: 14px; height: 14px; flex: none; margin-top: 3px; fill: var(--light-on-navy); }
  .contacts .web { margin-top: 18px; font-weight: 600; letter-spacing: 1.5px; }

  .back-brand {
    position: absolute; top: 95px; left: 500px; width: 260px;
    color: var(--navy); font-weight: 600; font-size: 30px; letter-spacing: 2px; line-height: 1.15; text-transform: uppercase;
  }
  .back-tab { position: absolute; right: 0; top: 198px; width: 36px; height: 70px; background: var(--navy); }
  .addresses { position: absolute; top: 300px; left: 490px; list-style: none; }
  .addresses li {
    display: flex; gap: 14px; color: var(--grey-text); font-size: 14px; letter-spacing: 1px; line-height: 1.4; margin-bottom: 14px;
  }
  .addresses svg { width: 11px; height: 15px; flex: none; margin-top: 2px; fill: var(--navy); }
</style>
</head>
<body>
<main class="sheet">

  <section class="card card-front" aria-label="Card front">
    <div class="edge edge-left"></div>
    <div class="edge edge-right"></div>
    <div class="front-brand">Norland<small>Advisory</small></div>
    <p class="disclaimer">Investment advisor services offered through Meridian Private Capital, LLC, an SEC registered investment advisor</p>
    <p class="front-web">www.norlandadvisory.com</p>
  </section>

  <section class="card card-back" aria-label="Card back">
    <div class="back-panel">
      <div class="person">
        <p class="person-name">Daniel Marlowe</p>
        <p class="person-title">Financial Advisor</p>
      </div>
      <ul class="contacts">
        <li>
          <svg viewBox="0 0 24 24"><path d="M6.6 10.8a15.1 15.1 0 0 0 6.6 6.6l2.2-2.2a1 1 0 0 1 1-.25 11.4 11.4 0 0 0 3.6.57 1 1 0 0 1 1 1V20a1 1 0 0 1-1 1A17 17 0 0 1 3 4a1 1 0 0 1 1-1h3.5a1 1 0 0 1 1 1c0 1.25.2 2.45.57 3.6a1 1 0 0 1-.25 1z"/></svg>
          <span>555-214-0380 Westbrook<br>555-302-4417 Eastfield</span>
        </li>
        <li>
          <svg viewBox="0 0 24 24"><path d="M2 5h20v14H2z M2 5l10 8 10-8" fill="none" stroke="#e9edf2" stroke-width="2"/></svg>
          <span>daniel@norlandadvisory.com</span>
        </li>
        <li class="web">
          <svg viewBox="0 0 24 24"><circle cx="12" cy="12" r="10"/></svg>
          <span>www.norlandadvisory.com</span>
        </li>
      </ul>
    </div>
    <div class="back-brand">Norland Advisory</div>
    <div class="back-tab"></div>
    <ul class="addresses">
      <li>
        <svg viewBox="0 0 12 16"><path d="M6 0a6 6 0 0 1 6 6c0 4.5-6 10-6 10S0 10.5 0 6a6 6 0 0 1 6-6zm0 3.5a2.5 2.5 0 1 0 0 5 2.5 2.5 0 0 0 0-5z"/></svg>
        <span>2240 Harbor Lane, Suite 410<br>Westbrook, Texas 75011</span>
      </li>
      <li>
        <svg viewBox="0 0 12 16"><path d="M6 0a6 6 0 0 1 6 6c0 4.5-6 10-6 10S0 10.5 0 6a6 6 0 0 1 6-6zm0 3.5a2.5 2.5 0 1 0 0 5 2.5 2.5 0 0 0 0-5z"/></svg>
        <span>88 Cedar Park Ave, Suite 630<br>Eastfield, Texas 75090</span>
      </li>
    </ul>
  </section>

</main>
</body>
</html>
```